Carwash Signage

We own and operate a 25m tunnel car wash in the uk. We are looking to upgrade our signage to include the following:-

Wash selection Board Size-1300x1300mm
Conditions 1300x1300mm
Instructions 1300x1300mm
Banner 2600x600mm
Stamp card flyer a5 double sided - 9 squares for stamping 3rd square needs to say free air freshener 9th square needs to say free vip car wash.

I have attached some notes for the details that are required to be included.

We are looking for a modern smart look more European car wash style than American car wash style. It should be bold and clear. with yellow/orange & blue/green,grey colours

The final design must be in a industry standard printable format.

UPDATED BRIEF AS DISCUSSED: We require design for 2 x window decals, flag design and 50% off voucher. Attached are rough layout drawings of what they should look like - we expect the designs to be in keeping with the previous designs colours, etc that have been carried out. We Look forward to hearing from you.

Target Market(s)

local car owners within a 15-20 mile radius

Colors
0054AA
0677BA
7BADD7
CADEEF
E8F1F8
0094D4
00A9DD
6FCCEA
C7EBF8
E9F6FB
00AB8E
00BBA5
67D7C9
C6EFE9
E9F9F6

Requirements
Must have
• must be sharp and modern European look

```html
<!DOCTYPE html>
<html lang="en">
<head>
<meta charset="utf-8">
<title>Solano Car Wash – Signage Set</title>
<link href="https://fonts.googleapis.com/css2?family=Montserrat:wght@600;700;800&family=Oswald:wght@500;600&family=Poppins:wght@500;600;700&family=Russo+One&display=swap" rel="stylesheet">
<style>
:root{
  --navy:#0b1f68;
  --navy-2:#0d2d78;
  --teal-deep:#0a7f92;
  --teal:#1fd3bf;
  --teal-soft:#67d7c9;
  --white:#ffffff;
  --ink:#0b1f68;
  --tick:#0054aa;
  --red:#e32222;
  --field:#e9f6fb;
  --page:#ffffff;
}
*{box-sizing:border-box;margin:0;padding:0}
html,body{width:1200px;height:728px;overflow:hidden;background:var(--page)}
body{position:relative;font-family:"Poppins",sans-serif;color:var(--white)}
.panel{position:absolute;overflow:hidden}
.grad-h{background:linear-gradient(90deg,var(--navy) 0%,var(--navy-2) 45%,var(--teal-deep) 100%)}
.grad-v{background:linear-gradient(180deg,var(--navy) 0%,var(--navy-2) 50%,var(--teal-deep) 100%)}
.abs{position:absolute}

/* brand lockup */
.brand{position:absolute;text-align:right;font-family:"Montserrat",sans-serif;font-weight:800;color:var(--white);line-height:1}
.brand .tag{display:block;font-weight:600;letter-spacing:.28em}
.brand .name{display:block;letter-spacing:.02em}

.display{font-family:"Russo One",sans-serif;font-style:italic;transform:skewX(-12deg);letter-spacing:.04em}
.cond{font-family:"Oswald",sans-serif;font-weight:600}

/* banner */
.banner{left:81px;top:107px;width:655px;height:151px}
.banner .divider{left:403px;top:12px;width:1px;height:126px;background:rgba(255,255,255,.35)}
.hours{position:absolute;left:414px;width:226px;text-align:center;font-family:"Russo One",sans-serif;line-height:1}
.hours .day{color:var(--teal);font-size:15px}
.hours .time{font-size:26px}
.pay{position:absolute;display:flex;align-items:center;gap:3px}
.pay .label{font-family:"Oswald",sans-serif;font-weight:600;color:var(--white);margin-right:5px}
.card-badge{background:var(--white);color:var(--ink);font-family:"Oswald",sans-serif;font-weight:600;display:flex;align-items:center;justify-content:center}

/* flyer */
.flyer{left:782px;top:69px;width:161px;height:228px}
.flyer-photo{left:0;top:0;width:161px;height:68px;background:linear-gradient(160deg,#0b3f6e,#0f7fa0 55%,#0b2f5a)}
.flyer-wave{left:0;top:52px;width:161px;height:22px}
.thumb{left:101px;width:51px;height:33px;border:1px solid var(--white)}
.flyer-foot{left:0;top:215px;width:161px;height:13px;background:var(--teal);color:var(--ink);font-size:4.6px;display:flex;align-items:center;justify-content:space-around;font-family:"Poppins",sans-serif;font-weight:500}

/* loyalty card */
.loyalty{left:957px;top:69px;width:161px;height:228px}
.consent{left:10px;top:36px;width:142px;font-size:3.1px;line-height:1.35;color:var(--white)}
.optin{left:10px;top:58px;font-size:4.2px;display:flex;align-items:center;gap:3px}
.optin i{display:block;width:6px;height:6px;background:var(--white)}
.field{left:10px;width:143px;height:6px;display:flex;gap:3px}
.field b{width:41px;background:var(--teal);color:var(--ink);font-size:3.4px;font-weight:600;text-align:right;padding-right:2px;line-height:6px}
.field span{flex:1;background:var(--white)}
.stamp{width:42px;height:31px;background:var(--white);border:1.5px solid var(--teal-soft);border-radius:3px;color:#9aa6b8;font-size:5px;display:flex;align-items:center;justify-content:center;text-align:center;line-height:1.15;font-family:"Montserrat",sans-serif;font-weight:600}

/* boards */
.board{top:333px;width:327px;height:327px}
.board-instr{left:81px}
.board-cond{left:436px}
.board-wash{left:791px}
.board-title{position:absolute;left:0;width:100%;top:67px;text-align:center;color:var(--teal);font-size:22px}

.steps{position:absolute;left:17px;width:300px;font-size:10.2px;font-weight:600;line-height:1.05;list-style:none}
.steps li{position:absolute;left:0;padding-left:14px;width:300px}
.steps li::before{content:"";position:absolute;left:0;top:2px;border-left:5px solid var(--white);border-top:4px solid transparent;border-bottom:4px solid transparent}
.icons{position:absolute;display:flex;align-items:flex-start}
.icon-cell{display:flex;flex-direction:column;align-items:center;text-align:center;font-family:"Russo One",sans-serif;line-height:1;color:var(--white)}
.icon-cell + .icon-cell{border-left:1px solid rgba(255,255,255,.55)}
.pict{background:var(--teal);border-radius:4px;opacity:.9}
.rules{left:17px;top:255px;width:293px;height:15px;background:var(--white);border-radius:8px;color:#111;font-size:7.6px;font-weight:600;display:flex;align-items:center;justify-content:center;gap:7px}
.rules em{font-style:normal;width:1px;height:9px;background:var(--tick)}
.tab{left:56px;top:305px;width:215px;height:24px;background:var(--teal);border-radius:10px 10px 0 0;color:var(--white);display:flex;align-items:center;justify-content:center;font-size:13px}

.notice{left:60px;top:77px;width:258px;text-align:center;font-size:9.3px;font-weight:600;line-height:1.2}
.help{left:14px;top:263px;width:300px;text-align:center;font-size:9.3px;font-weight:600;line-height:1.42}
.cond-cell{width:70px;font-size:7px}

/* wash selection table */
.wash-table{position:absolute;left:13px;top:97px;border-collapse:collapse;background:var(--white);color:var(--ink);table-layout:fixed}
.wash-table th,.wash-table td{border:1px solid var(--navy);text-align:center;vertical-align:middle}
.wash-table thead th{height:35px;font-family:"Oswald",sans-serif;font-size:4.3px;font-weight:600;line-height:1.05;text-transform:uppercase}
.wash-table .vert{writing-mode:vertical-rl;transform:rotate(180deg);font-size:6px}
.wash-table .vert-price{writing-mode:vertical-rl;transform:rotate(180deg);font-size:9px}
.wash-table tbody td{height:26px;font-size:8px}
.wash-table .tier{font-family:"Oswald",sans-serif;font-size:7px;font-weight:600;line-height:.9}
.wash-table .tier small{display:block;font-size:3.5px}
.tick{color:var(--tick);font-size:11px;font-weight:700}
.no{font-family:"Poppins",sans-serif;font-size:7px}
.price{font-family:"Oswald",sans-serif;font-weight:600;font-size:16px;letter-spacing:-.02em}
.price sup{font-size:7px;vertical-align:top;position:relative;top:-2px}
.offers{left:13px;top:241px;width:301px;height:50px;display:flex;gap:2px}
.offers div{background:var(--teal);color:var(--ink);display:flex;flex-direction:column;align-items:center;justify-content:center;text-align:center;line-height:1}
.red{color:var(--red)}
</style>
</head>
<body>

<!-- Banner -->
<section class="panel banner grad-h">
  <div class="brand" style="left:32px;top:17px;width:340px">
    <span class="tag" style="font-size:16px;margin-bottom:6px">CAR WASH</span>
    <span class="name" style="font-size:46px">SOLANO</span>
  </div>
  <div class="pay" style="left:36px;top:106px">
    <span class="label" style="font-size:17.5px">CASH + CARD PAYMENTS ACCEPTED</span>
    <span class="card-badge" style="width:37px;height:25px;font-size:8.5px">PAYCARD</span>
    <span class="card-badge" style="width:37px;height:25px;font-size:8.5px">CARDLINE</span>
  </div>
  <div class="abs divider"></div>
  <div class="hours" style="top:14px"><span class="display" style="display:inline-block;font-size:32px">OPEN</span></div>
  <div class="hours day" style="top:52px">MON - SAT</div>
  <div class="hours time" style="top:70px">8:00 - 18:00</div>
  <div class="hours day" style="top:102px">SUNDAY</div>
  <div class="hours time" style="top:118px">9:00 - 18:00</div>
</section>

<!-- Flyer -->
<section class="panel flyer grad-v">
  <div class="abs flyer-photo" role="img" aria-label="Photo of a car passing through the wash tunnel brushes"></div>
  <svg class="abs flyer-wave" viewBox="0 0 161 22" preserveAspectRatio="none"><path d="M0 8 Q40 22 90 12 T161 4 V22 H0Z" fill="var(--navy)"/><path d="M0 10 Q40 24 90 14 T161 6" stroke="var(--teal)" stroke-width="2" fill="none"/></svg>
  <div class="brand" style="left:15px;top:20px;width:132px">
    <span class="tag" style="font-size:6.5px;margin-bottom:2px">CAR WASH</span>
    <span class="name" style="font-size:20px">SOLANO</span>
  </div>
  <div class="abs display" style="left:12px;top:86px;font-size:13px">OPEN</div>
  <div class="abs" style="left:10px;top:101px;width:80px;font-family:'Russo One',sans-serif;line-height:1">
    <div style="color:var(--teal);font-size:5.5px;padding-left:16px">MON - SAT</div>
    <div style="font-size:10px">8:00 - 18:00</div>
    <div style="color:var(--teal);font-size:5.5px;padding-left:20px;margin-top:2px">SUNDAY</div>
    <div style="font-size:10px">9:00 - 18:00</div>
  </div>
  <div class="abs" style="left:9px;top:141px;line-height:1.05;font-weight:500">
    <div style="font-size:5.2px">V.I.P PLATINUM WASH PACK</div>
    <div style="font-size:7.6px">BUY 2 GET 1 FREE</div>
    <div style="font-size:13px;font-weight:700">£20.00</div>
    <div style="font-size:5.5px;margin-top:3px">LOYALTY CARD AVAILABLE</div>
    <div style="font-size:10.5px;font-weight:700">WASH + EARN</div>
    <div style="font-size:4.2px">ASK THE OPERATOR FOR DETAILS</div>
  </div>
  <div class="abs thumb" style="top:88px;background:linear-gradient(135deg,#6f8aa0,#d8e2ea)" role="img" aria-label="Photo of a smiling driver at the wheel"></div>
  <div class="abs thumb" style="top:125px;background:linear-gradient(135deg,#7bb6d6,#e9f6fb)" role="img" aria-label="Photo of a car wheel on the conveyor track"></div>
  <div class="abs thumb" style="top:162px;background:linear-gradient(135deg,#0f6fa8,#6fccea)" role="img" aria-label="Photo of an alloy wheel being sprayed with foam"></div>
  <svg class="abs" style="left:0;top:198px" width="161" height="18" viewBox="0 0 161 18" preserveAspectRatio="none"><path d="M0 10 Q50 0 100 8 T161 6 V18 H0Z" fill="var(--teal)"/></svg>
  <div class="abs flyer-foot"><span>☎ +00 123 456</span><span>◍ www.web.com</span><span>✉ contact@mail.com</span></div>
</section>

<!-- Loyalty card -->
<section class="panel loyalty grad-v">
  <div class="brand" style="left:50px;top:7px;width:60px">
    <span class="tag" style="font-size:3.5px;margin-bottom:1px">CAR WASH</span>
    <span class="name" style="font-size:9.5px">SOLANO</span>
  </div>
  <div class="abs display" style="left:12px;top:22px;font-size:12px">LOYALTY CARD</div>
  <p class="abs consent">By sharing your details you agree that we may store and use them to run this loyalty card and, if you opt in, to send you offers by email or text. See our privacy policy online for full details.</p>
  <div class="abs optin"><i></i>agree to receive future offer and marketing communications</div>
  <div class="abs field" style="top:68px"><b>First Name :</b><span></span></div>
  <div class="abs field" style="top:78px"><b>Surname :</b><span></span></div>
  <div class="abs field" style="top:87px"><b>Mobile Number :</b><span></span></div>
  <div class="abs field" style="top:96px"><b>Email Address :</b><span></span></div>
  <div class="abs field" style="top:105px"><b>Registration Number :</b><span></span></div>
  <svg class="abs" style="left:0;top:170px" width="161" height="58" viewBox="0 0 161 58" preserveAspectRatio="none"><path d="M0 30 Q40 18 80 28 T161 22 V58 H0Z" fill="var(--teal)"/></svg>
  <div class="abs stamp" style="left:10px;top:117px">1</div>
  <div class="abs stamp" style="left:60px;top:117px">2</div>
  <div class="abs stamp" style="left:110px;top:117px">FREE AIR<br>FRESHENER</div>
  <div class="abs stamp" style="left:10px;top:154px">4</div>
  <div class="abs stamp" style="left:60px;top:154px">5</div>
  <div class="abs stamp" style="left:110px;top:154px">6</div>
  <div class="abs stamp" style="left:10px;top:191px">7</div>
  <div class="abs stamp" style="left:60px;top:191px">8</div>
  <div class="abs stamp" style="left:110px;top:191px;font-size:6px">FREE<br>VIP CAR<br>WASH</div>
</section>

<!-- Instructions board -->
<section class="panel board board-instr grad-v">
  <div class="brand" style="left:56px;top:15px;width:212px">
    <span class="tag" style="font-size:12px;margin-bottom:4px">CAR WASH</span>
    <span class="name" style="font-size:30px">SOLANO</span>
  </div>
  <div class="board-title"><span class="display" style="display:inline-block">INSTRUCTIONS</span></div>
  <ul class="steps" style="top:101px">
    <li style="top:0">CHECK FOR LOOSE ITEMS BEFORE ENTERING THE WASH</li>
    <li style="top:16px">LOWER AERIAL (if electrical make sure the aerial is fully retracted, operator may assist but is not responsible for the replacement of your car)</li>
    <li style="top:55px">DRIVE FORWARD UNTIL OPERATOR TELLS YOU TO STOP</li>
    <li style="top:71px">OPERATOR WILL GUIDE YOU INTO THE CARWASH</li>
    <li style="top:87px">ONCE ON CONVEYOR TRACK :</li>
  </ul>
  <div class="icons" style="left:22px;top:203px;width:288px">
    <div class="icon-cell" style="width:58px;font-size:5px;height:46px"><div class="pict" style="width:22px;height:22px;margin-bottom:3px" role="img" aria-label="Handbrake pictogram"></div>HAND<br>BRAKE OFF<br>1</div>
    <div class="icon-cell" style="width:56px;font-size:5px;height:46px"><div class="pict" style="width:22px;height:22px;margin-bottom:2px" role="img" aria-label="Gear lever in neutral pictogram"></div>SELECT<br>NEUTRAL<br>GEAR<br>2</div>
    <div class="icon-cell" style="width:58px;font-size:5px;height:46px"><div class="pict" style="width:22px;height:20px;margin-bottom:3px" role="img" aria-label="Car door with closed window pictogram"></div>CLOSE ALL<br>WINDOWS &amp;<br>SUNROOF<br>3</div>
    <div class="icon-cell" style="width:60px;font-size:5px;height:46px"><div class="pict" style="width:22px;height:22px;margin-bottom:6px" role="img" aria-label="Running engine pictogram"></div>LEAVE ENGINE<br>RUNNING<br>4</div>
    <div class="icon-cell" style="width:56px;font-size:5px;height:46px"><div class="pict" style="width:22px;height:22px;margin-bottom:6px" role="img" aria-label="Windscreen wiper pictogram"></div>TURN AUTO<br>WIPERS OFF<br>5</div>
  </div>
  <div class="abs rules">DO NOT BRAKE<em></em>DO NOT STEER<em></em>DO NOT ATTEMPT EXIT VEHICLE</div>
  <ul class="steps" style="top:278px">
    <li style="top:0">AT END OF WASH, DRIVE AWAY WHEN TRAFFIC LIGHT TURNS GREEN</li>
  </ul>
  <div class="abs tab"><span class="display" style="display:inline-block">ENJOY THE RIDE</span></div>
</section>

<!-- Conditions board -->
<section class="panel board board-cond grad-v">
  <div class="brand" style="left:56px;top:15px;width:212px">
    <span class="tag" style="font-size:12px;margin-bottom:4px">CAR WASH</span>
    <span class="name" style="font-size:30px">SOLANO</span>
  </div>
  <svg class="abs" style="left:21px;top:79px" width="36" height="29" viewBox="0 0 36 29"><path d="M18 1 L35 28 H1 Z" fill="#ffd400" stroke="#222" stroke-width="1.2" stroke-linejoin="round"/><rect x="16.4" y="9" width="3.2" height="11" rx="1.2" fill="#111"/><circle cx="18" cy="23.6" r="1.8" fill="#111"/></svg>
  <p class="abs notice">SOLANO CAR + COMMERCIALS LTD.<br>CANNOT ACCEPT ANY RESPONSIBILITY FOR INJURY,<br>LOSS OR DAMAGE CAUSED BY THE FOLLOWING:</p>
  <div class="icons" style="left:23px;top:126px">
    <div class="icon-cell cond-cell" style="height:50px;font-size:6px"><div class="pict" style="width:30px;height:27px;margin-bottom:4px" role="img" aria-label="Car aerial pictogram"></div>NON-FULLY<br>RETRACTABLE<br>AERIALS</div>
    <div class="icon-cell cond-cell" style="height:50px;font-size:8px"><div class="pict" style="width:36px;height:27px;margin-bottom:4px" role="img" aria-label="Roof rack pictogram"></div>ROOF<br>RACKS</div>
    <div class="icon-cell cond-cell" style="height:50px;font-size:6.5px"><div class="pict" style="width:24px;height:30px;margin-bottom:4px" role="img" aria-label="Damaged car door pictogram"></div>DAMAGED<br>BODYWORK</div>
    <div class="icon-cell cond-cell" style="height:50px;font-size:8px"><div class="pict" style="width:24px;height:27px;margin-bottom:4px" role="img" aria-label="Loose door trim pictogram"></div>LOOSE<br>TRIMS</div>
  </div>
  <div class="icons" style="left:58px;top:190px">
    <div class="icon-cell cond-cell" style="height:54px;font-size:6.5px"><div class="pict" style="width:30px;height:22px;margin-bottom:5px" role="img" aria-label="Wing mirror pictogram"></div>LOOSE<br>WING<br>MIRRORS</div>
    <div class="icon-cell cond-cell" style="height:54px;font-size:6.5px"><div class="pict" style="width:32px;height:24px;margin-bottom:3px" role="img" aria-label="Exhaust pipe pictogram"></div>LOOSE<br>EXHAUST<br>SYSTEMS</div>
    <div class="icon-cell cond-cell" style="height:54px;font-size:8px"><div class="pict" style="width:32px;height:20px;margin-bottom:5px" role="img" aria-label="Cracked windscreen pictogram"></div>CRACKED<br>SHIELDS</div>
  </div>
  <p class="abs help">REMEMBER THE OPERATOR IS HERE TO HELP IF IN DOUBT.<br>PLEASE ASK FOR ADVICE BEFORE ENTERING THE WASH.<br>CLAIMS FOR DAMAGE CANNOT BE ENTERTAINED ONCE<br>VEHICLE HAS LEFT SITE.</p>
</section>

<!-- Wash selection board -->
<section class="panel board board-wash grad-v">
  <div class="brand" style="left:56px;top:15px;width:212px">
    <span class="tag" style="font-size:12px;margin-bottom:4px">CAR WASH</span>
    <span class="name" style="font-size:30px">SOLANO</span>
  </div>
  <div class="board-title"><span class="display" style="display:inline-block">WASH SELECTION</span></div>
  <table class="wash-table">
    <colgroup><col style="width:24px"><col span="10" style="width:24.6px"><col style="width:31px"></colgroup>
    <thead><tr>
      <th><span class="vert">OPTIONS</span></th>
      <th>Roof brush &amp; contour brushes sill brushes</th>
      <th>Drying (squeegee contour)</th>
      <th>Waxing (polish)</th>
      <th>Hand prepared</th>
      <th>Wax brush foam</th>
      <th>Alloy wheel spray</th>
      <th>Klaro ultra wax</th>
      <th>Jet wash prewash</th>
      <th>Under body wash</th>
      <th>Snow foam prewash</th>
      <th><span class="vert-price">PRICE</span></th>
    </tr></thead>
    <tbody>
      <tr><td class="tier">V.I.P<small>PLATINUM</small></td><td class="tick">✓</td><td class="tick">✓</td><td class="tick">✓</td><td class="tick">✓</td><td class="tick">✓</td><td class="tick">✓</td><td class="tick">✓</td><td class="tick">✓</td><td class="tick">✓</td><td class="tick">✓</td><td class="price"><sup>£</sup>10</td></tr>
      <tr><td class="tier">GOLD</td><td class="tick">✓</td><td class="tick">✓</td><td class="tick">✓</td><td class="tick">✓</td><td class="tick">✓</td><td class="tick">✓</td><td class="tick">✓</td><td class="tick">✓</td><td class="no">X</td><td class="no">X</td><td class="price"><sup>£</sup>8.5</td></tr>
      <tr><td class="tier">SILVER</td><td class="tick">✓</td><td class="tick">✓</td><td class="tick">✓</td><td class="tick">✓</td><td class="tick">✓</td><td class="no">X</td><td class="no">X</td><td class="no">X</td><td class="no">X</td><td class="no">X</td><td class="price"><sup>£</sup>7.5</td></tr>
      <tr><td class="tier">BRONZE</td><td class="tick">✓</td><td class="tick">✓</td><td class="tick">✓</td><td class="tick">✓</td><td class="no">X</td><td class="no">X</td><td class="no">X</td><td class="no">X</td><td class="no">X</td><td class="no">X</td><td class="price"><sup>£</sup>6.5</td></tr>
    </tbody>
  </table>
  <div class="abs offers">
    <div style="width:71px"><span class="cond" style="font-size:17px">OFFERS</span></div>
    <div style="width:113px;font-weight:600">
      <span style="font-size:7px">V.I.P PLATINUM WASH PACK</span>
      <span class="cond red" style="font-size:13px;margin:1px 0">BUY 2 GET 1 FREE</span>
      <span style="font-size:13px;font-weight:700">£20.00</span>
    </div>
    <div style="width:115px;font-weight:600">
      <span style="font-size:7px">LOYALTY CARD AVAILABLE</span>
      <span class="cond red" style="font-size:15px;margin:1px 0">WASH + EARN</span>
      <span style="font-size:5.5px;font-weight:500">ASK THE OPERATOR FOR DETAILS</span>
    </div>
  </div>
  <div class="pay" style="left:18px;top:299px">
    <span class="label" style="font-size:14.5px">CASH + CARD PAYMENTS ACCEPTED</span>
    <span class="card-badge" style="width:31px;height:20px;font-size:6.5px">PAYCARD</span>
    <span class="card-badge" style="width:31px;height:20px;font-size:6.5px">CARDLINE</span>
  </div>
</section>

</body>
</html>
```